KVT bottled water label

We are from The KVT Corner (TKC) - a university campus-retail initiative. As part of our branding exercise, we would like to produce a new range of bottled water and need a new label design carrying the following headline: "U Shape A Bolder U" (primary headline) with "Every Street Is Your Class" as the sub-headline (secondary headline).
Usage Of Line:
Emphasis must be given to the primary headline, and must not be placed before or on top of the primary headline. The reader must first read the primary headline before reading the secondary headline (assuming the reader reads from left to right and top to bottom.)
THE CONCEPT BEHIND OUR LINE:
Some Background:
Perceived as a fast-rising star since our inception in 2000, Pelrow Enterprise College challenged the Singapore education landscape - long dominated by an established field of long-tenured universities – by providing a holistic, broad-based and cross-disciplinary form of education that incorporates global exposure, internships and networking opportunities to prepare our students for real-world challenges - an experiential learning environment which we’ve proudly pioneered. Watch these videos from our graduates sharing their KVT experiences: http://kvt.example/22
When our first batch of graduates started their careers in 2004, employers saw a different breed of leaders. The graduates from KVT were bold, confident, articulate, versatile, well-rounded and eager for challenges. Today, more than 10,000 graduates across the world are testament to our trademark holistic and interactive approach to education. Our graduate employment record has been, and continues to be, robust with 60% finding jobs before graduation, and close to 100% getting employed within six months of graduation. Watch employers from Zentrik, QLV, RMO & HJK at: http://kvt.example/21
That is why we invite prospective students to Discover A Different 'U' - the letter 'U' can be interpreted to mean the 'U'niversity or 'U' as an individual (the prospective student).
The New Line:
With our new headline "U Shape A Bolder U - Every Street Is Your Class", we now pose the challenge back to our prospective students, and invite them to make a difference. How different their university experience can be, and how much they can be transformed, is limited only by their imagination.
For more information on KVT, please visit our website at: kvt.example.edu
Design:
The design must be vibrant and fresh to appeal to our students (from 18 years of age), yet still fit in perfectly on a table for a board of professionals and executive directors.
Audience:
It should appeal to the general masses, from our students to distinguished guests and executive directors to KVT.
Things to include (Requirements):
1. KVT logo (as below) must be included)
https://files.example.net/s/qq41wd/KVT%20Formal%20Logo.zip
2. Only 4 colours can be used (white is considered one color)
3. Must design within perimeters of working file:
https://files.example.net/s/pp73rk/bottled%20water%20working%20file.pdf
References
http://kvt.example/1m
http://kvt.example/1o
http://kvt.example/1p
http://kvt.example/1q
http://kvt.example/1r
http://kvt.example/1s
http://kvt.example/1t
http://kvt.example/1u
http://kvt.example/1v
http://kvt.example/1w
http://kvt.example/1x
http://kvt.example/1y

```html
<!DOCTYPE html>
<html lang="en">
<head>
<meta charset="utf-8">
<title>KVT Bottled Water Label</title>
<link rel="stylesheet" href="https://fonts.googleapis.com/css2?family=Montserrat:wght@800&family=Pinyon+Script&family=Roboto:wght@400;700&display=swap">
<style>
  :root {
    --page-bg: #e9edf2;
    --navy: #163a66;
    --deep-blue: #1f4f85;
    --mid-blue: #3b7bb8;
    --light-blue: #7fb0dc;
    --magenta: #d62a7c;
    --white: #ffffff;
    --ink: #1b1b1b;
  }
  * { margin: 0; padding: 0; box-sizing: border-box; }
  html, body {
    width: 960px;
    height: 1200px;
    overflow: hidden;
    background: var(--page-bg);
  }
  .canvas {
    position: relative;
    width: 960px;
    height: 1200px;
  }
  .label {
    position: absolute;
    left: 20px;
    top: 470px;
    width: 920px;
    height: 260px;
    overflow: hidden;
    background: linear-gradient(180deg, var(--navy) 0%, var(--deep-blue) 26%, var(--mid-blue) 40%, var(--light-blue) 100%);
  }
  .ornament {
    position: absolute;
    top: 0;
    height: 260px;
  }
  .ornament--left {
    left: 0;
    width: 150px;
    background: radial-gradient(circle at 55% 60%, var(--magenta) 0%, #e86aa6 30%, var(--white) 42%, var(--mid-blue) 58%, var(--deep-blue) 100%);
  }
  .ornament--middle {
    left: 600px;
    width: 100px;
    background: radial-gradient(circle at 50% 58%, var(--white) 0%, var(--magenta) 35%, var(--mid-blue) 70%, var(--deep-blue) 100%);
  }
  .headline-zone {
    position: absolute;
    left: 150px;
    top: 0;
    width: 450px;
    height: 260px;
    text-align: center;
  }
  .headline {
    margin-top: 28px;
    font-family: "Montserrat", sans-serif;
    font-weight: 800;
    font-size: 30px;
    line-height: 36px;
    letter-spacing: 0.5px;
    color: var(--white);
    white-space: nowrap;
  }
  .subheadline {
    margin-top: 26px;
    font-family: "Pinyon Script", cursive;
    font-size: 36px;
    line-height: 44px;
    color: var(--navy);
    white-space: nowrap;
  }
  .brand-mark {
    display: inline-flex;
    align-items: center;
    gap: 8px;
    margin-top: 22px;
    font-family: "Montserrat", sans-serif;
    font-weight: 800;
    font-size: 22px;
    color: var(--navy);
  }
  .brand-mark__square {
    width: 18px;
    height: 18px;
    background: var(--navy);
  }
  .nutrition-panel {
    position: absolute;
    left: 704px;
    top: 14px;
    width: 204px;
    height: 232px;
    background: var(--white);
    padding: 8px 9px;
    font-family: "Roboto", sans-serif;
    font-size: 8px;
    line-height: 1.3;
    color: var(--ink);
  }
  .nutrition-panel__product {
    font-weight: 700;
    font-size: 9px;
    margin-bottom: 3px;
  }
  .nutrition-table {
    width: 100%;
    border-collapse: collapse;
    border: 1px solid var(--ink);
    margin-bottom: 4px;
  }
  .nutrition-table th,
  .nutrition-table td {
    padding: 1px 3px;
    text-align: left;
    font-weight: 400;
  }
  .nutrition-table caption {
    text-align: left;
    font-weight: 700;
    font-size: 9px;
    border: 1px solid var(--ink);
    border-bottom: none;
    padding: 1px 3px;
  }
  .nutrition-table .row-divider td { border-top: 1px solid var(--ink); }
  .nutrition-table .col-head th { border-top: 1px solid var(--ink); font-weight: 700; }
  .nutrition-panel__note { margin-bottom: 3px; }
  .nutrition-panel__tech {
    font-weight: 700;
    margin-top: 4px;
  }
  .nutrition-panel__maker {
    font-family: "Roboto", sans-serif;
    font-weight: 700;
    font-size: 15px;
    color: var(--ink);
  }
</style>
</head>
<body>
<main class="canvas">
  <section class="label">
    <div class="ornament ornament--left" role="img" aria-label="Pink, white and blue paisley swirl ornament"></div>

    <div class="headline-zone">
      <h1 class="headline">U SHAPE A BOLDER U</h1>
      <p class="subheadline">Every Street Is Your Class</p>
      <div class="brand-mark"><span class="brand-mark__square"></span>KVT</div>
    </div>

    <div class="ornament ornament--middle" role="img" aria-label="Pink and white paisley swirl ornament"></div>

    <aside class="nutrition-panel">
      <p class="nutrition-panel__product">Oxygenated Drinking Water</p>
      <table class="nutrition-table">
        <caption>Nutrition Information</caption>
        <tr class="row-divider"><td colspan="3">Servings per package: 1</td></tr>
        <tr><td colspan="3">Serving size: 500ml</td></tr>
        <tr class="col-head"><th></th><th>per serving</th><th>per 100ml</th></tr>
        <tr class="row-divider"><td>Energy</td><td>0 kcal</td><td>0 kcal</td></tr>
        <tr><td>Protein</td><td>0 g</td><td>0 g</td></tr>
        <tr><td>Fat</td><td>0 g</td><td>0 g</td></tr>
        <tr><td>Carbohydrate</td><td>0 g</td><td>0 g</td></tr>
      </table>
      <p class="nutrition-panel__note">Not a significant source of dietary fibre, saturated fat and cholesterol.</p>
      <p class="nutrition-panel__note">Manufactured in Singapore for Brightwell Waters Pte Ltd, 8 Fernvale Road<br>Tel: 6000 0000 Fax: 6000 0001<br>Email: hello@brightwell.example</p>
      <p class="nutrition-panel__tech">Produced Using The Technology of</p>
      <p class="nutrition-panel__maker">OXYVA Singapore</p>
    </aside>
  </section>
</main>
</body>
</html>
```